Online business manager needs a website

I need a website designed and then coded. I am an online business manager serving a number of different industries providing administrative support to existing small businesses and helping solo practitioners get their new business up and running.

I didn't have a logo formally designed but have been using the attached avatar and wouldn't mind something that incorporated that.

The business doesn't have an official name, so I've just been using my name Lia Morvath, Online Business Manager or Lia Morvath, OBM. I've attached two documents that I have made previously for an example of content.

I would prefer the final site be in Wordpress.

Requirements
Must have
• A way to contact me, testimonials, list of services

```html
<!DOCTYPE html>
<html lang="en">
<head>
<meta charset="utf-8">
<title>Lia Morvath — Online Business Manager</title>
<link href="https://fonts.googleapis.com/css2?family=Marcellus&family=Lato:wght@400;700;900&display=swap" rel="stylesheet">
<style>
:root{
  --purple:#4b1a8c;
  --purple-deep:#341066;
  --purple-soft:#6a2fb0;
  --night:#1f0f3b;
  --ink:#333;
  --muted:#777;
  --light:#f6f6f6;
  --star:#f5b400;
  --white:#fff;
}
*{margin:0;padding:0;box-sizing:border-box}
html,body{width:1200px;height:3810px;overflow:hidden}
body{position:relative;font-family:"Lato",sans-serif;color:var(--ink);background:var(--white)}
.abs{position:absolute}
svg.ic{display:inline-block;vertical-align:middle}

/* header */
.topbar{left:0;top:0;width:1200px;height:9px;background:var(--purple)}
.brand{left:111px;top:22px}
.brand .name{font-family:"Marcellus",serif;font-size:40px;color:var(--purple);line-height:1}
.brand .sub{font-size:14px;color:#555;letter-spacing:1.5px;margin-top:4px}
.topcontact{left:636px;top:21px;font-size:12px;font-weight:700;color:#222;display:flex;gap:22px;align-items:center}
.topcontact .sep{color:#999}
.nav{left:542px;top:70px;display:flex;gap:48px;font-size:14px;color:#333}
.nav .active{color:var(--purple);font-weight:700;text-decoration:underline}
.btn-contact{left:963px;top:62px;width:125px;height:38px;background:var(--purple);color:#fff;font-weight:700;font-size:15px;border-radius:12px 0 12px 0;display:flex;align-items:center;justify-content:center}

/* hero */
.hero{left:0;top:111px;width:1200px;height:555px;background:radial-gradient(ellipse at 35% 40%,#3b2260 0%,#1c1030 55%,#120a20 100%)}
.hero-photo{left:540px;top:111px;width:660px;height:555px;background:linear-gradient(135deg,#5a3a6a 0%,#b78a6a 45%,#6d5470 100%)}
.hero-welcome{left:111px;top:210px;color:#fff;font-family:"Marcellus",serif;font-size:26px;letter-spacing:6px}
.hero-title{left:111px;top:252px;color:#fff;font-family:"Marcellus",serif;font-size:76px;line-height:1;font-weight:400}
.hero-text{left:111px;top:346px;width:440px;color:#fff;font-size:15px;line-height:30px}
.btn-start{left:111px;top:459px;width:175px;height:49px;background:#fff;color:var(--purple);font-family:"Marcellus",serif;font-size:17px;border-radius:22px 0 22px 0;display:flex;align-items:center;justify-content:center}
.hero-dots{left:114px;top:569px;display:flex;gap:6px}
.hero-dots span{width:12px;height:12px;border:1.5px solid #fff;border-radius:50%}
.hero-dots span.on{background:#fff}

/* about */
.about-block{left:0;top:747px;width:391px;height:610px;background:linear-gradient(160deg,#5a22a0,#3a0f78)}
.about-photo{left:112px;top:824px;width:415px;height:450px;border:3px solid #fff;outline:1px solid #ccc;background:linear-gradient(150deg,#7a2a55 0%,#c0607a 40%,#2e2a28 100%)}
.about-title{left:614px;top:794px;font-family:"Marcellus",serif;font-size:42px;font-weight:400;color:var(--purple)}
.kicker{font-size:18px;letter-spacing:4px;font-weight:700;color:#555}
.about-kicker{left:614px;top:861px}
.about-text{left:614px;top:893px;width:468px;font-size:14.5px;line-height:29px;color:#333}
.about-call{left:614px;top:1202px;font-size:18px;font-weight:700;color:var(--purple)}
.btn-read{left:614px;top:1249px;width:176px;height:51px;background:var(--purple);color:#fff;font-family:"Marcellus",serif;font-size:17px;border-radius:22px 0 22px 0;display:flex;align-items:center;justify-content:center;box-shadow:3px 4px 0 #ddd}

/* services */
.services{left:0;top:1440px;width:1200px;height:648px;background:var(--light)}
.sec-title{width:1200px;text-align:center;font-family:"Marcellus",serif;font-size:43px;font-weight:400;color:var(--purple)}
.sec-kicker{width:1200px;text-align:center}
.card{width:297px;height:398px;background:#fff;border-radius:6px;box-shadow:0 2px 6px rgba(0,0,0,.08);top:1610px}
.card .img{position:absolute;left:0;top:0;width:297px;height:234px;border-radius:6px 6px 0 0}
.card .body{position:absolute;left:12px;top:198px;width:273px;height:190px;background:#fff;border-radius:6px 6px 0 0;text-align:center;padding-top:14px}
.card h3{font-family:"Marcellus",serif;font-size:20px;color:#222;line-height:29px;font-weight:400}
.card p{font-size:14px;color:#777;line-height:26px;margin-top:2px}
.card a{display:block;font-size:15px;color:#222;font-weight:700;text-decoration:underline;margin-top:10px}
.arrow{width:32px;height:32px;border-radius:50%;top:1792px;display:flex;align-items:center;justify-content:center}

/* contact */
.contact{left:0;top:2088px;width:1200px;height:472px;background:linear-gradient(100deg,#4b1a8c 0%,#5b24a6 55%,#3d1280 100%)}
.laptop{left:115px;top:2138px;width:412px;height:352px;background:linear-gradient(180deg,#d8c9a8 0%,#6fb37a 50%,#8a8a8a 100%);border-radius:10px}
.contact-title{left:611px;top:2154px;font-family:"Marcellus",serif;font-size:43px;font-weight:400;color:#fff}
.contact-kicker{left:611px;top:2219px}
.contact-text{left:611px;top:2256px;width:462px;color:#fff;font-size:14.5px;line-height:30px}
.btn-call{left:611px;top:2424px;width:228px;height:50px;background:#fff;color:var(--purple);font-family:"Marcellus",serif;font-size:17px;border-radius:22px 0 22px 0;display:flex;align-items:center;justify-content:center}

/* testimonials */
.avatar{border-radius:50%;background:linear-gradient(135deg,#c79b7a,#6b4a3a)}
.t-main{left:529px;top:2741px;width:142px;height:142px;border:4px solid var(--purple);background:linear-gradient(135deg,#8fb36a,#c86a5a 60%,#5a3a2a)}
.t-name{left:0;top:2897px;width:1200px;text-align:center;font-family:"Marcellus",serif;font-size:26px;color:#222}
.t-role{left:0;top:2938px;width:1200px;text-align:center;font-size:13px;color:#666;font-weight:700}
.t-stars{left:0;top:2966px;width:1200px;text-align:center;color:var(--star);font-size:30px;letter-spacing:1px}
.t-text{left:255px;top:3007px;width:690px;text-align:center;font-size:15px;line-height:29px;color:#333}
.quote{font-family:Georgia,serif;font-size:230px;line-height:1;color:#ddd;font-weight:700}
.t-dots{left:562px;top:3133px;display:flex;gap:8px}
.t-dots span{width:12px;height:12px;border-radius:50%;background:#c9cdf0}
.t-dots span.on{background:var(--purple)}

/* footer */
.footer{left:0;top:3229px;width:1200px;height:581px;background:var(--night)}
.field{top:3309px;width:240px;height:58px;border:1.5px solid #fff;border-radius:10px 0 10px 0;color:#fff;font-size:13px;font-weight:700;padding-left:20px;display:flex;align-items:center}
.btn-submit{left:923px;top:3309px;width:165px;height:56px;background:#fff;color:var(--purple);font-family:"Marcellus",serif;font-size:19px;border-radius:22px 0 22px 0;display:flex;align-items:center;justify-content:center}
.rule{left:111px;width:977px;height:1px;background:#5a4a78}
.f-brand{left:111px;top:3468px;color:#fff}
.f-brand .name{font-family:"Marcellus",serif;font-size:46px;line-height:1}
.f-brand .sub{font-size:16px;letter-spacing:1.5px;margin-top:8px;font-weight:700}
.social{top:3576px;width:32px;height:32px;border-radius:50%;background:var(--purple)}
.f-col h4{font-family:"Marcellus",serif;font-size:20px;color:#fff;font-weight:400;margin-bottom:14px}
.f-col li{list-style:none;color:#fff;font-size:15px;height:34px;display:flex;align-items:center;gap:12px}
.f-contact li{height:auto;align-items:flex-start;margin-bottom:18px;line-height:27px}
.ci{width:32px;height:32px;border-radius:50%;background:var(--purple);display:flex;align-items:center;justify-content:center;flex:none}
.copy{left:0;top:3765px;width:1200px;text-align:center;color:#fff;font-size:15px}
</style>
</head>
<body>

<div class="abs topbar"></div>
<div class="abs brand"><div class="name">Lia Morvath</div><div class="sub">Online Business Manager</div></div>
<div class="abs topcontact">
  <span><svg class="ic" width="12" height="12" viewBox="0 0 24 24"><path fill="#4b1a8c" d="M6.6 10.8a15 15 0 006.6 6.6l2.2-2.2c.3-.3.7-.4 1-.2 1.1.4 2.3.6 3.6.6.6 0 1 .4 1 1V20c0 .6-.4 1-1 1A17 17 0 013 4c0-.6.4-1 1-1h3.5c.6 0 1 .4 1 1 0 1.3.2 2.5.6 3.6.1.3 0 .7-.2 1z"/></svg>&nbsp; Phone : 5550142876</span>
  <span class="sep">|</span>
  <span><svg class="ic" width="14" height="11" viewBox="0 0 24 18"><path fill="#4b1a8c" d="M0 0h24v18H0z"/><path fill="none" stroke="#fff" stroke-width="2" d="M1 1l11 9 11-9"/></svg>&nbsp; Email : lia.morvath@mailbox.example</span>
</div>
<nav class="abs nav"><span class="active">Home</span><span>About Me</span><span>Services</span><span>Testimonials</span></nav>
<div class="abs btn-contact">Contact Me</div>

<section class="abs hero"></section>
<div class="abs hero-photo" role="img" aria-label="Portrait photo of Lia smiling against a starry purple background"></div>
<div class="abs hero-welcome">WELCOME TO</div>
<h1 class="abs hero-title">LIA MORVATH</h1>
<p class="abs hero-text">Helping businesses achieve their goals is my passion, and I'm thrilled that with my assistance you will have more time for your own passion project.</p>
<div class="abs btn-start">GET STARTED</div>
<div class="abs hero-dots"><span></span><span class="on"></span><span></span><span></span></div>

<div class="abs about-block"></div>
<div class="abs about-photo" role="img" aria-label="Photo of Lia wearing glasses in front of pink flowers"></div>
<h2 class="abs about-title">Hii, I am Lia Morvath</h2>
<div class="abs kicker about-kicker">ONLINE BUSINESS MANAGER</div>
<div class="abs about-text">
  <p>Hi! I'm so excited that you have chosen to explore my portfolio.<br>Helping businesses achieve their goals is my passion, and I'm thrilled that with my assistance you will have more time for your own passion project. I thrive while working independently, which means you can be confident when leaving tasks for me. The type of work that lights me up is anything involving organization and/or spreadsheets.</p>
  <p style="margin-top:29px">You need data analyzed that includes multiple nested if formulas? You have an overwhelming amount of email to sort through and appointments to book? I'm your gal!</p>
</div>
<div class="abs about-call"><svg class="ic" width="15" height="15" viewBox="0 0 24 24"><path fill="#4b1a8c" d="M6.6 10.8a15 15 0 006.6 6.6l2.2-2.2c.3-.3.7-.4 1-.2 1.1.4 2.3.6 3.6.6.6 0 1 .4 1 1V20c0 .6-.4 1-1 1A17 17 0 013 4c0-.6.4-1 1-1h3.5c.6 0 1 .4 1 1 0 1.3.2 2.5.6 3.6.1.3 0 .7-.2 1z"/></svg> Call Us : 5550142876</div>
<div class="abs btn-read">READ MORE</div>

<section class="abs services"></section>
<h2 class="abs sec-title" style="left:0;top:1496px">Our Services</h2>
<div class="abs kicker sec-kicker" style="left:0;top:1559px">WHAT WE OFFER</div>

<div class="abs arrow" style="left:34px;background:#9b7fc0"><svg width="12" height="14" viewBox="0 0 12 14"><path d="M8 2L3 7l5 5" fill="none" stroke="#fff" stroke-width="2.4"/></svg></div>
<div class="abs arrow" style="left:1126px;background:var(--purple)"><svg width="12" height="14" viewBox="0 0 12 14"><path d="M4 2l5 5-5 5" fill="none" stroke="#fff" stroke-width="2.4"/></svg></div>

<article class="abs card" style="left:111px">
  <div class="img" role="img" aria-label="Photo of a woman working at a laptop" style="background:linear-gradient(135deg,#8aa07a,#d6a24a 55%,#f0e6d8)"></div>
  <div class="body"><h3>Virtual Assistance</h3><p>Calendar Management, Email Management, Light Graphic Design, Data Entry, Temporibus autem quibusdam et aut officiis.</p><a>Read More</a></div>
</article>
<article class="abs card" style="left:451px">
  <div class="img" role="img" aria-label="Photo of hands typing on a keyboard with content icons" style="background:linear-gradient(135deg,#3a3a3a,#7a7a7a 55%,#b0b0b0)"></div>
  <div class="body"><h3>Social Media &amp; Content Management</h3><p>Content Repurposing Graphics, Creation Audiogram Creation, Search Engine Optimization.</p><a>Read More</a></div>
</article>
<article class="abs card" style="left:792px">
  <div class="img" role="img" aria-label="Photo of colleagues reviewing a tablet in an office" style="background:linear-gradient(135deg,#9aa8b0,#5a6470 55%,#c8b8a8)"></div>
  <div class="body"><h3>Finance Management</h3><p>CCreate Invoices Track Receivables Analyze Expenses Year Over Year Analytics rerum necessitatibus saepe eveniet ut et voluptates.</p><a>Read More</a></div>
</article>

<section class="abs contact"></section>
<div class="abs laptop" role="img" aria-label="Illustration of a cartoon avatar waving from a laptop screen"></div>
<h2 class="abs contact-title">Contact Me</h2>
<div class="abs kicker contact-kicker" style="color:#fff">LIA MORVATH</div>
<div class="abs contact-text">
  <p>Focused on the live event and entertainment industry.</p>
  <p style="margin-top:30px">Helping artists and owners to better manage their career and business by strategically reviewing systems, recommending operational efficiencies, and managing inboxes.</p>
</div>
<div class="abs btn-call">Call Us: 5550142876</div>

<h2 class="abs sec-title" style="left:0;top:2623px">What Customer Says</h2>
<div class="abs kicker sec-kicker" style="left:0;top:2686px">TESTIMONIALS</div>
<div class="abs avatar" style="left:121px;top:2822px;width:68px;height:68px;background:linear-gradient(135deg,#f0d0b0,#c0906a)" role="img" aria-label="Customer photo"></div>
<div class="abs avatar" style="left:1000px;top:2748px;width:48px;height:48px" role="img" aria-label="Customer photo"></div>
<div class="abs" style="left:367px;top:2860px;width:13px;height:13px;border-radius:50%;background:var(--purple)"></div>
<div class="abs" style="left:882px;top:2822px;width:6px;height:6px;border-radius:50%;background:#222"></div>
<div class="abs avatar t-main" role="img" aria-label="Photo of customer Dana R."></div>
<div class="abs quote" style="left:150px;top:2905px">&ldquo;</div>
<div class="abs quote" style="left:958px;top:3005px">&rdquo;</div>
<div class="abs t-name">Dana R.</div>
<div class="abs t-role">Owner, Northgate Roofing</div>
<div class="abs t-stars">★★★★★</div>
<p class="abs t-text">When it became apparent that a project would take more time than I had, Lia stepped up to take on the required research. She was thorough and timely; able to meet a last-minute 12-hour deadline. I would highly recommend Lia to assist with your next project.</p>
<div class="abs t-dots"><span></span><span class="on"></span><span></span><span></span></div>

<footer class="abs footer"></footer>
<div class="abs field" style="left:111px">Name</div>
<div class="abs field" style="left:380px">Email</div>
<div class="abs field" style="left:648px">Phone</div>
<div class="abs btn-submit">SUBMIT</div>
<div class="abs rule" style="top:3423px"></div>

<div class="abs f-brand"><div class="name">Lia Morvath</div><div class="sub">Online Business Manager</div></div>
<div class="abs social" style="left:111px" aria-label="Social link"></div>
<div class="abs social" style="left:169px" aria-label="Social link"></div>
<div class="abs social" style="left:227px" aria-label="Social link"></div>
<div class="abs social" style="left:284px" aria-label="Social link"></div>

<div class="abs f-col" style="left:423px;top:3473px">
  <h4>Quick Links</h4>
  <ul>
    <li><svg width="14" height="12" viewBox="0 0 14 12"><path d="M0 6h11M7 1l5 5-5 5" fill="none" stroke="#fff" stroke-width="2"/></svg>Home</li>
    <li><svg width="14" height="12" viewBox="0 0 14 12"><path d="M0 6h11M7 1l5 5-5 5" fill="none" stroke="#fff" stroke-width="2"/></svg>About Me</li>
    <li><svg width="14" height="12" viewBox="0 0 14 12"><path d="M0 6h11M7 1l5 5-5 5" fill="none" stroke="#fff" stroke-width="2"/></svg>Services</li>
    <li><svg width="14" height="12" viewBox="0 0 14 12"><path d="M0 6h11M7 1l5 5-5 5" fill="none" stroke="#fff" stroke-width="2"/></svg>Testimonials</li>
    <li><svg width="14" height="12" viewBox="0 0 14 12"><path d="M0 6h11M7 1l5 5-5 5" fill="none" stroke="#fff" stroke-width="2"/></svg>Contact Me</li>
  </ul>
</div>
<div class="abs f-col" style="left:638px;top:3473px">
  <h4>Help Links</h4>
  <ul>
    <li><svg width="14" height="12" viewBox="0 0 14 12"><path d="M0 6h11M7 1l5 5-5 5" fill="none" stroke="#fff" stroke-width="2"/></svg>FAQ</li>
    <li><svg width="14" height="12" viewBox="0 0 14 12"><path d="M0 6h11M7 1l5 5-5 5" fill="none" stroke="#fff" stroke-width="2"/></svg>Terms of use</li>
    <li><svg width="14" height="12" viewBox="0 0 14 12"><path d="M0 6h11M7 1l5 5-5 5" fill="none" stroke="#fff" stroke-width="2"/></svg>Privacy Policy</li>
    <li><svg width="14" height="12" viewBox="0 0 14 12"><path d="M0 6h11M7 1l5 5-5 5" fill="none" stroke="#fff" stroke-width="2"/></svg>Support Links</li>
    <li><svg width="14" height="12" viewBox="0 0 14 12"><path d="M0 6h11M7 1l5 5-5 5" fill="none" stroke="#fff" stroke-width="2"/></svg>Conditions</li>
  </ul>
</div>
<div class="abs f-col f-contact" style="left:861px;top:3473px">
  <h4>Contact Me</h4>
  <ul>
    <li><span class="ci"><svg width="12" height="16" viewBox="0 0 12 16"><path fill="#fff" d="M6 0a6 6 0 016 6c0 4.5-6 10-6 10S0 10.5 0 6a6 6 0 016-6zm0 3.5a2.5 2.5 0 100 5 2.5 2.5 0 000-5z"/></svg></span><span>Lia Morvath<br>United States</span></li>
    <li><span class="ci"><svg width="14" height="14" viewBox="0 0 24 24"><path fill="#fff" d="M6.6 10.8a15 15 0 006.6 6.6l2.2-2.2c.3-.3.7-.4 1-.2 1.1.4 2.3.6 3.6.6.6 0 1 .4 1 1V20c0 .6-.4 1-1 1A17 17 0 013 4c0-.6.4-1 1-1h3.5c.6 0 1 .4 1 1 0 1.3.2 2.5.6 3.6.1.3 0 .7-.2 1z"/></svg></span><span style="line-height:32px">5550142876</span></li>
    <li><span class="ci"><svg width="14" height="11" viewBox="0 0 24 18"><path fill="#fff" d="M0 0h24v18H0z"/><path fill="none" stroke="#4b1a8c" stroke-width="2" d="M1 1l11 9 11-9"/></svg></span><span style="line-height:32px">lia.morvath@mailbox.example</span></li>
  </ul>
</div>
<div class="abs rule" style="top:3734px"></div>
<div class="abs copy">Copyright © 2023.Lia Morvath Online Business Manager. All Rights Reserved.</div>

</body>
</html>
```